Bramblecot Namecard

We have a regular but rotating group of Actors and Directors who meet weekly. I'd like to make a nametag (first and last names) for each of the participants which would fit on a regular business card. The first name would be over-sized to enable reading at a distance. The background & border should project fun and warmth. The Bramblecot is meant to be a place to play without judgement or negative vibes.

```html
<!DOCTYPE html>
<html lang="en">
<head>
<meta charset="utf-8">
<title>Bramblecot Namecard</title>
<link rel="stylesheet" href="https://fonts.googleapis.com/css2?family=Archivo+Black&family=Signika:wght@700&display=swap">
<style>
  :root {
    --sky-top: #1566b8;
    --sky-low: #2a9ed9;
    --sea-deep: #1aa9c9;
    --sea-light: #7fd8da;
    --foam: #e6f3ea;
    --sand: #f3e1c2;
    --sand-deep: #e9cfa6;
    --name-top: #fbb21c;
    --name-bottom: #ee5a1f;
    --shadow: #2b1a12;
    --white: #ffffff;
    --venue-red: #e3392a;
    --star-red: #d8261b;
  }
  html, body {
    margin: 0;
    padding: 0;
    overflow: hidden;
  }
  .namecard {
    position: relative;
    width: 1200px;
    height: 929px;
    overflow: hidden;
  }
  .beach-scene {
    position: absolute;
    inset: 0;
    background: linear-gradient(
      to bottom,
      var(--sky-top) 0%,
      var(--sky-low) 24%,
      var(--sea-deep) 27%,
      var(--sea-light) 46%,
      var(--foam) 56%,
      var(--sand) 62%,
      var(--sand-deep) 100%
    );
  }
  .starfish-area {
    position: absolute;
    left: 723px;
    top: 596px;
    width: 325px;
    height: 235px;
    border-radius: 50%;
    background: radial-gradient(ellipse at center, var(--star-red) 0%, rgba(216, 38, 27, 0.6) 45%, rgba(216, 38, 27, 0) 72%);
  }
  .first-name,
  .last-name,
  .venue {
    position: absolute;
    left: 40px;
    margin: 0;
    line-height: 1;
    white-space: nowrap;
  }
  .first-name {
    top: 276px;
    font-family: "Archivo Black", "Arial Black", sans-serif;
    font-size: 160px;
    letter-spacing: 1px;
    background: linear-gradient(to bottom, var(--name-top) 20%, var(--name-bottom) 85%);
    -webkit-background-clip: text;
    background-clip: text;
    color: transparent;
    filter: drop-shadow(6px 7px 0 var(--shadow));
  }
  .last-name {
    top: 448px;
    font-family: "Archivo Black", "Arial Black", sans-serif;
    font-size: 82px;
    color: var(--white);
    letter-spacing: 1px;
    filter: drop-shadow(3px 4px 0 rgba(43, 26, 18, 0.35));
  }
  .venue {
    top: 527px;
    left: 44px;
    font-family: "Signika", sans-serif;
    font-weight: 700;
    font-size: 88px;
    color: var(--venue-red);
    filter: drop-shadow(4px 4px 0 var(--shadow));
  }
</style>
</head>
<body>
  <main class="namecard">
    <div class="beach-scene" role="img" aria-label="Sunny tropical beach with blue sky, sun glare, palm leaves and turquoise sea over pale sand"></div>
    <div class="starfish-area" role="img" aria-label="Red starfish and small shells lying on the sand"></div>
    <h1 class="first-name">CORDELIA</h1>
    <p class="last-name">WYNTERS</p>
    <p class="venue">The Bramblecot</p>
  </main>
</body>
</html>
```